Business card design needed

We are a wine business involved in winemaking, broking and packaging on behalf of clients globally with the majority being Asian. The design should be quite traditional and classic with some red used, font used should be easily read.

Target Market(s)

Trade customers other business owners

Industry/Entity Type

Business

Contact Information for Business Card

Rosalind Whitcombe
Meridale Wine Collective
PO Box 738, Fenwick Vale
Western Australia 6318
Phone: +61 (0)487 263 918
Email: mvcellar@brindlenet.com.au

Logo styles of interest
Lettermark Logo

```html
<!DOCTYPE html>
<html lang="en">
<head>
<meta charset="utf-8">
<title>Rosalind Whitcombe – Business Card</title>
<link rel="stylesheet" href="https://fonts.googleapis.com/css2?family=Pinyon+Script&family=Tinos&display=swap">
<style>
  :root {
    --backdrop: #a3a3a3;
    --wood-light: #7a3c14;
    --wood-mid: #3e1b0a;
    --wood-dark: #0e0604;
    --cream: #f4ead8;
    --script-cream: #f2e2c0;
    --wine-red: #9b1b36;
  }
  html, body {
    margin: 0;
    padding: 0;
    width: 1200px;
    height: 1000px;
    overflow: hidden;
    background: var(--backdrop);
  }
  .canvas {
    position: relative;
    width: 1200px;
    height: 1000px;
  }
  .business-card {
    position: absolute;
    left: 70px;
    top: 156px;
    width: 1065px;
    height: 614px;
    box-shadow: 0 6px 18px rgba(0, 0, 0, 0.45);
    overflow: hidden;
  }
  .wood-texture {
    position: absolute;
    inset: 0;
    background:
      radial-gradient(ellipse 55% 65% at 56% 52%, var(--wood-light) 0%, var(--wood-mid) 55%, var(--wood-dark) 100%);
  }
  .brand-mark {
    position: absolute;
    left: 130px;
    top: 200px;
    width: 165px;
    display: flex;
    flex-direction: column;
    align-items: center;
    gap: 14px;
  }
  .brand-dot {
    width: 70px;
    height: 70px;
    border-radius: 50%;
    background: var(--wine-red);
  }
  .brand-name {
    font-family: "Tinos", "Times New Roman", serif;
    font-size: 26px;
    color: var(--cream);
    letter-spacing: 0.5px;
  }
  .card-details {
    position: absolute;
    left: 400px;
    top: 180px;
    font-family: "Tinos", "Times New Roman", serif;
    color: var(--cream);
    font-size: 26px;
    line-height: 40px;
  }
  .person-name {
    margin: 0 0 2px 0;
    font-family: "Pinyon Script", cursive;
    font-weight: 400;
    font-size: 70px;
    line-height: 80px;
    color: var(--script-cream);
    text-shadow: 1px 2px 2px rgba(0, 0, 0, 0.6);
    white-space: nowrap;
  }
  .company, .postal-line {
    margin: 0 0 0 4px;
  }
  .contact-block {
    margin: 42px 0 0 10px;
  }
  .contact-block p {
    margin: 0;
    white-space: nowrap;
  }
</style>
</head>
<body>
<main class="canvas">
  <section class="business-card">
    <div class="wood-texture" role="img" aria-label="Dark oak wood grain background with a warm amber glow at the centre"></div>

    <div class="brand-mark">
      <div class="brand-dot"></div>
      <div class="brand-name">Meridale</div>
    </div>

    <div class="card-details">
      <h1 class="person-name">Rosalind Whitcombe</h1>
      <p class="company">Meridale Wine Collective</p>
      <p class="postal-line">PO Box</p>
      <div class="contact-block">
        <p class="address">738, Fenwick Vale Western Australia 6318</p>
        <p class="phone">Phone: +61 (0)487 263 918</p>
        <p class="email">Email: mvcellar@brindlenet.com.au</p>
      </div>
    </div>
  </section>
</main>
</body>
</html>
```